Criação de Folder para Alimentos & Bebidas
A empresa queria:
" importamos produtos com nossas marcas e distribuimos para supermercdos e distribuidores "

```html
<!DOCTYPE html>
<html lang="pt-BR">
<head>
<meta charset="UTF-8">
<title>Meridia Foods — Folder</title>
<link rel="stylesheet" href="https://fonts.googleapis.com/css2?family=Open+Sans:wght@400;600&display=swap">
<style>
  :root {
    --stage: #2b2b2d;
    --panel: #0b0b0c;
    --panel-edge: #161617;
    --gold: #c9a24a;
    --gold-light: #f0d58a;
    --gold-dark: #7a5a1f;
    --red: #b3201c;
    --text: #f2f2f2;
    --muted: #bdbdbd;
  }
  * { margin: 0; padding: 0; box-sizing: border-box; }
  html, body { width: 1200px; height: 1200px; overflow: hidden; }
  body {
    background: var(--stage);
    font-family: "Open Sans", Arial, sans-serif;
    display: flex;
    align-items: center;
    justify-content: center;
  }
  .folder {
    display: flex;
    width: 1100px;
    height: 760px;
    box-shadow: 0 20px 50px rgba(0,0,0,.55);
  }
  .panel {
    position: relative;
    width: 550px;
    height: 100%;
    background: var(--panel);
    overflow: hidden;
  }
  .panel--back { border-right: 1px solid var(--panel-edge); }

  .brand {
    position: absolute;
    left: 0; right: 0;
    text-align: center;
    color: var(--text);
    font-weight: 600;
    letter-spacing: .5px;
  }
  .brand-dot {
    display: inline-block;
    width: .45em; height: .45em;
    border-radius: 50%;
    background: var(--red);
    margin: 0 .3em .08em;
    vertical-align: middle;
  }

  /* back cover */
  .panel--back .brand { top: 520px; font-size: 34px; }
  .contact {
    position: absolute;
    top: 600px; left: 44px; right: 30px;
    display: flex;
    justify-content: space-between;
    color: var(--muted);
    font-size: 11px;
    line-height: 1.45;
  }
  .contact-item { display: flex; align-items: center; gap: 7px; }
  .contact-icon {
    width: 18px; height: 18px;
    border-radius: 50%;
    background: var(--red);
    display: flex; align-items: center; justify-content: center;
    flex-shrink: 0;
  }
  .contact-icon svg { width: 10px; height: 10px; fill: #fff; }

  .gold-band {
    position: absolute;
    left: 0; right: 0;
    bottom: 48px;
    height: 18px;
    background: linear-gradient(90deg, var(--gold-dark), var(--gold-light) 30%, var(--gold) 60%, var(--gold-dark));
  }
  .gold-band::after {
    content: "";
    position: absolute;
    left: 0; right: 0; top: 22px;
    height: 2px;
    background: var(--gold-dark);
  }

  /* front cover */
  .panel--front .brand { top: 58px; font-size: 30px; }
  .rule {
    position: absolute;
    left: 0; right: 0;
    height: 3px;
    background: var(--red);
  }
  .rule::after {
    content: "";
    position: absolute;
    left: 0; right: 0;
    height: 1px;
    background: var(--gold);
  }
  .rule--top { top: 128px; }
  .rule--top::after { top: -6px; }
  .rule--bottom { top: 416px; }
  .rule--bottom::after { bottom: -6px; }
  .photo {
    position: absolute;
    left: 0; right: 0;
    top: 136px; height: 276px;
    background:
      radial-gradient(ellipse at 30% 65%, #7a2a17 0%, transparent 45%),
      radial-gradient(ellipse at 72% 62%, #6b2314 0%, transparent 42%),
      radial-gradient(ellipse at 55% 25%, #3d5a22 0%, transparent 40%),
      radial-gradient(ellipse at 88% 30%, #b87a22 0%, transparent 35%),
      linear-gradient(180deg, #3a1a10, #1a0d08);
  }
  .mark {
    position: absolute;
    top: 520px; left: 50%;
    width: 14px; height: 14px;
    margin-left: -7px;
    border-radius: 50%;
    background: var(--red);
  }
</style>
</head>
<body>
  <main class="folder">
    <section class="panel panel--back">
      <div class="brand">Meridia<span class="brand-dot"></span>Foods</div>
      <div class="contact">
        <div class="contact-item">
          <span class="contact-icon"><svg viewBox="0 0 24 24"><path d="M6.6 10.8a15 15 0 0 0 6.6 6.6l2.2-2.2c.3-.3.7-.4 1-.2 1.1.4 2.3.6 3.6.6.6 0 1 .4 1 1V20c0 .6-.4 1-1 1A17 17 0 0 1 3 4c0-.6.4-1 1-1h3.5c.6 0 1 .4 1 1 0 1.3.2 2.5.6 3.6.1.3 0 .7-.2 1z"/></svg></span>
          <span>(11) 4032-5870<br>(11) 4032-5871</span>
        </div>
        <div class="contact-item">
          <span class="contact-icon"><svg viewBox="0 0 24 24"><path d="M12 2a7 7 0 0 0-7 7c0 5.2 7 13 7 13s7-7.8 7-13a7 7 0 0 0-7-7zm0 9.5a2.5 2.5 0 1 1 0-5 2.5 2.5 0 0 1 0 5z"/></svg></span>
          <span>R. das Palmeiras, 210<br>Campinas CEP: 13010-040</span>
        </div>
        <div class="contact-item">
          <span class="contact-icon"><svg viewBox="0 0 24 24"><path d="M2 5h20v14H2zm2 2v.5l8 5 8-5V7z"/></svg></span>
          <span>contato@meridiafoods.com.br<br>www.meridiafoods.com.br</span>
        </div>
      </div>
      <div class="gold-band"></div>
    </section>

    <section class="panel panel--front">
      <div class="brand">Meridia<span class="brand-dot"></span>Foods</div>
      <div class="rule rule--top"></div>
      <div class="photo" role="img" aria-label="Foto de bifes grelhados com tomates-cereja, ervas e batatas sobre tábua"></div>
      <div class="rule rule--bottom"></div>
      <div class="mark"></div>
      <div class="gold-band"></div>
    </section>
  </main>
</body>
</html>
```